Independence Day Graphics for Sale

I want to create 10 social media graphics (new Pictora size 4:5 (1080 x 1350 pixels) focusing on our July 4th Sale Graphics, using any of the pics attached. Use the attached pics, NO RANDOM STOCK PHOTOGRAPHY. For the color scheme of the graphics, they should all be complementary to the product colors in the photos.
You can add any of the photos attached but none are required. You can do some of the graphics in all text. I mainly need BOLD text that says one of the headlines (10 total) SEE ATTACHED WORD DOCUMENT for the headlines to use.

Target Market(s)

women looking to lose weight

Requirements
Must have
• pics attached and text attached

```html
<!DOCTYPE html>
<html lang="en">
<head>
<meta charset="utf-8">
<title>July 4th Mega Sale</title>
<link href="https://fonts.googleapis.com/css2?family=Bebas+Neue&family=Oswald:wght@500;700&display=swap" rel="stylesheet">
<style>
  :root {
    --red: #d62f3c;
    --navy: #2b2a72;
    --white: #ffffff;
    --yellow: #fcc41c;
    --yellow-dark: #e6a814;
    --ink: #111111;
    --shadow: rgba(60, 20, 25, 0.35);
  }
  * { margin: 0; padding: 0; box-sizing: border-box; }
  html, body { width: 960px; height: 1200px; overflow: hidden; }
  body { background: var(--red); font-family: "Bebas Neue", "Oswald", sans-serif; }

  .poster { position: relative; width: 960px; height: 1200px; background: var(--red); overflow: hidden; }

  .stars { position: absolute; left: 0; top: 72px; width: 960px; height: 36px; }

  .stamp { position: absolute; left: 66px; top: 172px; width: 590px; height: 820px; }

  .photo {
    position: absolute; left: 108px; top: 210px; width: 500px; height: 770px;
    background: linear-gradient(180deg, #f2eff6 0%, #ddd8e8 35%, #eeeeee 60%, #2a2a2a 100%);
    border-radius: 4px;
  }

  .headline { position: absolute; left: 0; top: 0; width: 960px; height: 1000px; font-weight: 400; }
  .headline span {
    position: absolute; display: block; white-space: nowrap;
    line-height: 1; transform-origin: right top;
    -webkit-text-stroke: 2px var(--red); paint-order: stroke fill;
    text-shadow: 6px 6px 0 var(--shadow);
  }
  .headline .line-july { font-size: 293px; top: 135px; right: 31px; color: var(--white); transform: scaleX(0.94); }
  .headline .line-date { font-size: 298px; top: 352px; right: 62px; color: var(--white); transform: scaleX(0.95); }
  .headline .line-mega { font-size: 242px; top: 589px; right: 36px; color: var(--yellow); transform: scaleX(0.96); }
  .headline .line-sale { font-size: 262px; top: 778px; right: 44px; color: var(--yellow); transform: scaleX(0.93); }

  .offer {
    position: absolute; left: -14px; top: 100px; width: 480px; height: 138px;
    background: var(--yellow); transform: rotate(-20deg); transform-origin: center;
    box-shadow: 0 6px 10px rgba(0,0,0,0.18);
    text-align: center;
  }
  .offer::after {
    content: ""; position: absolute; right: -26px; top: -34px; width: 40px; height: 80px;
    background: var(--yellow-dark); border-radius: 0 30px 10px 0;
  }
  .offer-amount { display: block; font-size: 128px; line-height: 1; color: var(--ink); margin-top: 4px; letter-spacing: -1px; }
  .offer-scope { display: block; font-family: "Oswald", sans-serif; font-weight: 500; font-size: 34px; line-height: 1; color: var(--ink); letter-spacing: 2px; margin-top: -8px; }

  .ticker {
    position: absolute; left: 0; top: 1058px; width: 960px; height: 102px;
    background: var(--navy); color: var(--white);
    display: flex; align-items: center; justify-content: center; gap: 24px;
    font-size: 96px; line-height: 1; padding-top: 8px;
  }
  .ticker .star { font-size: 50px; margin-top: -8px; }
</style>
</head>
<body>
<main class="poster">
  <svg class="stars" viewBox="0 0 960 36" aria-hidden="true">
    <defs>
      <polygon id="star" points="0,-17 4,-5.5 16.2,-5.3 6.5,2 10,14 0,7 -10,14 -6.5,2 -16.2,-5.3 -4,-5.5" fill="#ffffff"/>
    </defs>
    <use href="#star" x="71" y="18"/><use href="#star" x="151" y="18"/><use href="#star" x="229" y="18"/>
    <use href="#star" x="529" y="18"/><use href="#star" x="607" y="18"/><use href="#star" x="686" y="18"/>
    <use href="#star" x="773" y="18"/><use href="#star" x="853" y="18"/><use href="#star" x="920" y="18"/>
  </svg>

  <svg class="stamp" viewBox="0 0 590 820" aria-hidden="true">
    <defs>
      <pattern id="perf-h" width="22" height="14" patternUnits="userSpaceOnUse"><rect x="12" y="0" width="10" height="14" fill="#d62f3c"/></pattern>
      <pattern id="perf-v" width="14" height="22" patternUnits="userSpaceOnUse"><rect x="0" y="12" width="14" height="10" fill="#d62f3c"/></pattern>
    </defs>
    <rect x="0" y="0" width="590" height="820" fill="#ffffff"/>
    <rect x="0" y="0" width="590" height="14" fill="url(#perf-h)"/>
    <rect x="0" y="806" width="590" height="14" fill="url(#perf-h)"/>
    <rect x="0" y="0" width="14" height="820" fill="url(#perf-v)"/>
    <rect x="576" y="0" width="14" height="820" fill="url(#perf-v)"/>
  </svg>

  <div class="photo" role="img" aria-label="Smiling woman in a white cropped sweater holding a supplement bottle, with a lavender Statue of Liberty silhouette behind her and two supplement bottles in front"></div>

  <h1 class="headline">
    <span class="line-july">JULY</span>
    <span class="line-date">4TH</span>
    <span class="line-mega">MEGA</span>
    <span class="line-sale">SALE!</span>
  </h1>

  <div class="offer">
    <span class="offer-amount">25%OFF</span>
    <span class="offer-scope">EVERYTHING</span>
  </div>

  <div class="ticker">
    <span>SALE!</span><span class="star">★</span>
    <span>SALE!</span><span class="star">★</span>
    <span>SALE!</span><span class="star">★</span>
    <span>SALE!</span>
  </div>
</main>
</body>
</html>
```